Business Cards Design for the electrical wholesaler: clean bold dynamic :)

We need a business card design that would follow our latest brand guidelines. As an electrical wholesaler we want to bring a fresh look and feel into the industry. The design should be clean bold and dynamic. It should come alive with the renewed energy of our green colour. Our grey colour should keep things balanced and complement the notion of maturity and responsibility. We employ Lato as a corporate font however are not bound by this font and we’re open to interpretation here.

Target Market(s)

Electrical contractors

Industry/Entity Type

Business

Contact Information for Business Card

Logo
Name & Surname: Olena Dovbush
Job Title: Director of Marketing
Email: helen.dovbush@mailvane.example
Cell phone: XXX.XXX.XXXX
Address: 20917 - 87 Ave. Edmonton, AB, Canada. T6K 2R8
Business Phone: 780.555.0187
Website: www.qorvil.example

Font styles to use
Other font styles liked:
• Lato

Requirements
Must have
• Logo & website
Nice to have
• Brand elements - some of them you may find in the attached Brand Guidelines (e.g. three lines on the background signifying "W")

```html
<!DOCTYPE html>
<html lang="en">
<head>
<meta charset="utf-8">
<title>Qorvil business card</title>
<link href="https://fonts.googleapis.com/css2?family=Lato:wght@400;700&display=swap" rel="stylesheet">
<style>
  :root {
    --green: #84bd3a;
    --grey: #4a4a4c;
    --text: #555557;
    --paper: #f7f7f7;
    --backdrop: #bdbdbd;
    --rule: #7a7a7a;
  }
  * { margin: 0; padding: 0; box-sizing: border-box; }
  html, body { width: 1200px; height: 960px; overflow: hidden; }
  body {
    background: var(--backdrop);
    font-family: "Lato", Arial, sans-serif;
    position: relative;
  }
  .card {
    position: absolute;
    left: 320px;
    width: 600px;
    height: 340px;
    box-shadow: 0 3px 8px rgba(0,0,0,0.25);
  }
  .card-front { top: 100px; background: var(--green); }
  .card-back { top: 494px; background: var(--paper); }

  .front-brand {
    position: absolute;
    left: 0; right: 0; top: 118px;
    text-align: center;
    font-weight: 700;
    font-size: 76px;
    line-height: 1;
    color: #ffffff;
  }
  .front-web {
    position: absolute;
    left: 0; right: 0; top: 300px;
    text-align: center;
    color: #ffffff;
    font-size: 13px;
    letter-spacing: 3.4px;
  }

  .back-brand {
    position: absolute;
    right: 35px; top: 46px;
    display: flex; align-items: center; gap: 12px;
  }
  .brand-dot { width: 26px; height: 26px; border-radius: 50%; background: var(--green); }
  .brand-name { font-size: 46px; font-weight: 400; color: var(--grey); line-height: 1; }

  .name-tab {
    position: absolute; left: 0; top: 173px;
    width: 13px; height: 38px; background: var(--green);
  }
  .person { position: absolute; left: 37px; top: 171px; }
  .person-name { font-size: 20px; font-weight: 700; color: var(--green); line-height: 24px; }
  .person-title { font-size: 15px; color: var(--text); line-height: 20px; }
  .divider {
    position: absolute; left: 37px; top: 223px;
    width: 528px; height: 1px; background: var(--rule);
  }
  .contacts { position: absolute; left: 37px; top: 236px; list-style: none; }
  .contacts li {
    display: flex; align-items: center; gap: 9px;
    font-size: 14px; color: var(--text); line-height: 19px;
  }
  .contacts svg { width: 13px; height: 13px; fill: var(--green); flex: none; }
  .address {
    position: absolute; right: 34px; top: 257px;
    text-align: right; font-size: 14px; color: var(--text); line-height: 19px;
    font-style: normal;
  }
</style>
</head>
<body>
  <section class="card card-front">
    <div class="front-brand">qorvil</div>
    <div class="front-web">www.qorvil.example</div>
  </section>

  <section class="card card-back">
    <div class="back-brand">
      <span class="brand-dot"></span>
      <span class="brand-name">qorvil</span>
    </div>

    <div class="name-tab"></div>
    <div class="person">
      <div class="person-name">DANA WHITLOW</div>
      <div class="person-title">CEO/FOUNDER</div>
    </div>
    <div class="divider"></div>

    <ul class="contacts">
      <li>
        <svg viewBox="0 0 16 16" aria-hidden="true"><path d="M3.5 1 6 4 4.7 6c.9 2 2.3 3.4 4.3 4.3L11 9l3 2.5-1.5 2.8C6.5 14 2 9.5 1.7 3.5z"/></svg>
        555 014 2538
      </li>
      <li>
        <svg viewBox="0 0 16 16" aria-hidden="true"><path d="M4 0h8a1 1 0 0 1 1 1v14a1 1 0 0 1-1 1H4a1 1 0 0 1-1-1V1a1 1 0 0 1 1-1zm1 2v10h6V2zm3 11a1 1 0 1 0 0 2 1 1 0 0 0 0-2z"/></svg>
        555 016 9364
      </li>
      <li>
        <svg viewBox="0 0 16 16" aria-hidden="true"><path d="M4 1h8v4H4zM1 6h14v6h-2v-2H3v2H1zM4 11h8v4H4z"/></svg>
        555 019 1940
      </li>
      <li>
        <svg viewBox="0 0 16 16" aria-hidden="true"><path d="M1 3h14v1L8 9 1 4zm0 3 7 5 7-5v7H1z"/></svg>
        info@qorvil.example
      </li>
    </ul>

    <address class="address">
      42 Linden Crescent<br>
      Northvale, XX 00000<br>
      www.qorvil.example
    </address>
  </section>
</body>
</html>
```